need web page design for TarnwickHub.com

This site sells information products for international corporate users. It is selling Silent Rivers and Quiet Orchard Lanes, a product on international business tax, and other books. See sample. I will also upload a possible logo. Upload 2 The tag line is Predicting and Solving Business and Law Issues for the Multinational Upload 3 is a sample theme from Shopify, the site I will use. The sample is for ideas only. I am not wedded to it. Upload 4 is Copperfield Monthly Digest Pge

2 page

```html
<!DOCTYPE html>
<html lang="en">
<head>
<meta charset="utf-8">
<title>TarnwickHub.com</title>
<link href="https://fonts.googleapis.com/css2?family=Roboto:wght@400;500;700&family=Roboto+Slab:wght@400&family=Open+Sans:wght@400&display=swap" rel="stylesheet">
<style>
:root{
  --navy:#1e3f86;
  --band:#2a4a8a;
  --heading:#1f3b7a;
  --text:#333;
  --muted:#555;
  --grey-bg:#ececec;
  --footer:#2d2d2d;
  --white:#fff;
}
*{margin:0;padding:0;box-sizing:border-box}
html,body{width:942px;height:1200px;overflow:hidden;background:var(--white)}
body{position:relative;font-family:'Open Sans',sans-serif;color:var(--text)}
.abs{position:absolute}

/* header */
.site-header{left:0;top:0;width:942px;height:99px}
.brand{left:141px;top:30px;display:flex;align-items:center;gap:6px}
.brand-dot{width:30px;height:30px;border-radius:50%;background:var(--navy)}
.brand-name{font-family:'Roboto',sans-serif;font-weight:700;font-size:17px;color:var(--navy)}
.brand-tag{left:141px;top:66px;font-size:5px;color:var(--muted);font-family:'Roboto',sans-serif}
.main-nav{left:373px;top:37px;display:flex;align-items:center;font-family:'Roboto',sans-serif;font-size:10.5px;color:#333}
.main-nav a{color:inherit;text-decoration:none;padding:0 10px;line-height:25px}
.main-nav a.active{background:var(--navy);color:var(--white);border-radius:4px;padding:0 12px;margin-right:-4px}

/* hero */
.hero{left:0;top:99px;width:942px;height:419px;background:radial-gradient(ellipse at 50% 30%,#3f8f95 0%,#2a6b72 35%,#1b3f45 70%,#0d1f24 100%)}
.hero-title{left:0;top:260px;width:942px;text-align:center;font-family:'Roboto Slab',serif;font-weight:400;font-size:27px;line-height:39px;color:var(--white);letter-spacing:.3px}
.slide-arrow{top:287px;width:28px;height:28px;border-radius:50%;background:var(--white)}
.slide-arrow svg{display:block}

/* services */
.services{left:0;top:518px;width:942px;height:215px;background:var(--band)}
.service{width:160px;text-align:center;color:var(--white)}
.service-icon{width:62px;height:62px;border-radius:50%;background:var(--white);margin:0 auto;display:flex;align-items:center;justify-content:center;box-shadow:2px 3px 3px rgba(0,0,0,.35)}
.service h3{font-family:'Roboto Slab',serif;font-weight:400;font-size:14px;line-height:18px;margin-top:14px;text-transform:uppercase}
.service p{font-size:8.5px;line-height:13px;margin-top:8px}

/* intro */
.welcome-title,.clients-title,.blog-title{font-family:'Roboto Slab',serif;font-weight:400;font-size:14px;color:var(--heading);text-transform:uppercase}
.welcome-title{left:133px;top:755px}
.welcome-text{left:133px;top:783px;width:408px;font-size:9.6px;line-height:17.6px;text-align:justify;color:var(--text)}
.read-more{font-size:8.5px;color:var(--heading);text-decoration:none}
.divider{left:550px;top:757px;width:1px;height:110px;background:#e6e6e6}
.clients-title{left:575px;top:755px}
.client-photo{left:574px;top:784px;width:62px;height:62px;border-radius:50%;background:radial-gradient(circle at 50% 45%,#b58a6e 0%,#6d4a38 55%,#2a2a2a 100%)}
.client-name{left:645px;top:784px;font-size:8.5px;color:var(--heading)}
.client-text{left:646px;top:801px;width:158px;font-size:8.1px;line-height:13.5px;text-align:justify}

/* blog */
.blog{left:0;top:893px;width:942px;height:223px;background:var(--grey-bg)}
.blog-title{left:144px;top:914px}
.blog-nav{top:913px;width:17px;height:17px;border:1.5px solid #111;border-radius:50%}
.blog-card{top:939px;width:163px}
.blog-thumb{height:108px;border:3px solid var(--white);box-shadow:0 0 2px rgba(0,0,0,.3)}
.blog-card p{margin-top:13px;font-size:9.2px;line-height:14px;color:var(--muted);text-align:justify;padding:0 1px}

/* footer */
.site-footer{left:0;top:1116px;width:942px;height:84px;background:var(--footer)}
.copyright{left:135px;top:1149px;font-family:'Roboto',sans-serif;font-size:11px;color:#ddd}
.social{top:1140px;width:28px;height:28px;border-radius:50%;border:2px solid #ccc}
.footer-links{left:682px;top:1148px;font-family:'Roboto',sans-serif;font-size:11px;color:#ddd}
</style>
</head>
<body>

<header class="site-header abs">
  <div class="brand abs"><span class="brand-dot"></span><span class="brand-name">TarnwickHub.com</span></div>
  <div class="brand-tag abs">Business and law solutions for multinational firms</div>
  <nav class="main-nav abs">
    <a class="active" href="#">HOME</a><a href="#">TAX</a><a href="#">CUSTOMS</a><a href="#">FOREIGN INVESTMENTS</a><a href="#">CONTACT</a><a href="#">MEMBER AREA</a>
  </nav>
</header>

<section class="hero abs" role="img" aria-label="Team of business people standing in front of a world map"></section>
<h1 class="hero-title abs">PREDICTING AND SOLVING BUSINESS AND<br>LAW ISSUES FOR THE MULTINATIONALS</h1>
<div class="slide-arrow abs" style="left:34px"><svg width="28" height="28"><path d="M16 8 L10 14 L16 20" fill="none" stroke="#222" stroke-width="2"/></svg></div>
<div class="slide-arrow abs" style="left:875px"><svg width="28" height="28"><path d="M12 8 L18 14 L12 20" fill="none" stroke="#222" stroke-width="2"/></svg></div>

<section class="services abs">
  <div class="service abs" style="left:131px;top:28px">
    <div class="service-icon"><svg width="40" height="30" viewBox="0 0 40 30" fill="#1e3f86"><circle cx="9" cy="8" r="4"/><circle cx="20" cy="6" r="5"/><circle cx="31" cy="8" r="4"/><path d="M2 22 q7-10 14 0z"/><path d="M24 22 q7-10 14 0z"/><path d="M11 26 q9-14 18 0z"/></svg></div>
    <h3>Tax<br>Developments</h3>
    <p>Lorem Ipsum has been the industry's standard dummy text ever since the galley of type and scrambled</p>
  </div>
  <div class="service abs" style="left:303px;top:28px">
    <div class="service-icon"><svg width="36" height="36" viewBox="0 0 36 36" fill="none" stroke="#1e3f86" stroke-width="3.5"><circle cx="13" cy="13" r="6" stroke-dasharray="3 2"/><circle cx="27" cy="10" r="4" stroke-dasharray="2.5 1.5"/><circle cx="14" cy="28" r="4" stroke-dasharray="2.5 1.5"/></svg></div>
    <h3>Finance<br>Developments</h3>
    <p>Lorem Ipsum has been the industry's standard dummy text ever since the galley of type and scrambled</p>
  </div>
  <div class="service abs" style="left:477px;top:28px">
    <div class="service-icon"><svg width="36" height="36" viewBox="0 0 36 36" fill="none" stroke="#1e3f86" stroke-width="3"><circle cx="18" cy="18" r="15"/><path d="M6 12 q12 8 24 0 M6 24 q12-8 24 0 M18 3 q-8 15 0 30"/></svg></div>
    <h3>Customs<br>Developments</h3>
    <p>Lorem Ipsum has been the industry's standard dummy text ever since the galley of type and scrambled</p>
  </div>
  <div class="service abs" style="left:646px;top:28px">
    <div class="service-icon"><svg width="36" height="36" viewBox="0 0 36 36"><circle cx="20" cy="8" r="4" fill="none" stroke="#1e3f86" stroke-width="1.5"/><circle cx="27" cy="13" r="3.5" fill="none" stroke="#1e3f86" stroke-width="1.5"/><rect x="3" y="20" width="5" height="10" fill="none" stroke="#1e3f86" stroke-width="1.5"/><path d="M9 21 h10 q4 0 4 3 l9-4 q2 1 0 3 l-12 7 h-11z" fill="#1e3f86"/></svg></div>
    <h3>Foreign<br>Investments</h3>
    <p>Lorem Ipsum has been the industry's standard dummy text ever since the galley of type and scrambled</p>
  </div>
</section>

<h2 class="welcome-title abs">Welcome to TarnwickHub</h2>
<p class="welcome-text abs">Lorem ipsum dolor sit amet, consectetur adipiscing elit. Aenean nec orci urna, in pellentesque ipsum. Nam vitae odio a felis adipiscing rutrum. Maecenas sit amet tortor libero. Fusce gravida aliquet gravida. Nunc pretium, augue in ultricies pharetra, tortor nibh accumsan diam.Quisque</p>
<a class="read-more abs" href="#" style="left:486px;top:842px">Read More &gt;&gt;</a>
<div class="divider abs"></div>
<h2 class="clients-title abs">Clients</h2>
<div class="client-photo abs" role="img" aria-label="Portrait photo of a client"></div>
<div class="client-name abs">Mara Lindqvist</div>
<p class="client-text abs">Lorem ipsum dolor sit amet, consectetur adipiscing elit. Aenean nec orci urna, in pellentesque ipsum. Nam vitae odio a</p>
<a class="read-more abs" href="#" style="left:749px;top:845px">Read More &gt;&gt;</a>

<section class="blog abs"></section>
<h2 class="blog-title abs">Latest Blog</h2>
<div class="blog-nav abs" style="left:776px"><svg width="14" height="14"><path d="M8 4 L5 7 L8 10" fill="none" stroke="#111" stroke-width="1.5"/></svg></div>
<div class="blog-nav abs" style="left:798px"><svg width="14" height="14"><path d="M6 4 L9 7 L6 10" fill="none" stroke="#111" stroke-width="1.5"/></svg></div>

<article class="blog-card abs" style="left:143px">
  <div class="blog-thumb" role="img" aria-label="Glowing clock held in a hand" style="background:radial-gradient(circle at 55% 55%,#ffd27a 0%,#d98a1c 35%,#4a2a08 80%)"></div>
  <p>Lorem Ipsum is simply dummy text of the printing and typesetting</p>
</article>
<article class="blog-card abs" style="left:312px">
  <div class="blog-thumb" role="img" aria-label="Man standing before a wall of golden gears" style="background:radial-gradient(circle at 50% 45%,#f3d57a 0%,#b8893a 45%,#6d5a3a 100%)"></div>
  <p>Lorem Ipsum is simply dummy text of the printing and typesetting</p>
</article>
<article class="blog-card abs" style="left:481px;top:942px">
  <div class="blog-thumb" role="img" aria-label="Office team working at a desk" style="background:linear-gradient(135deg,#c9ccd1 0%,#8a8f96 50%,#3d4148 100%)"></div>
  <p>Lorem Ipsum is simply dummy text of the printing and typesetting</p>
</article>
<article class="blog-card abs" style="left:652px;top:942px">
  <div class="blog-thumb" role="img" aria-label="Two colleagues smiling in a meeting" style="background:linear-gradient(90deg,#b9b2a8 0%,#8c8780 50%,#2e3440 100%)"></div>
  <p>Lorem Ipsum is simply dummy text of the printing and typesetting</p>
</article>

<footer class="site-footer abs"></footer>
<div class="copyright abs">Copy right © 2014 All Rights</div>
<div class="social abs" style="left:428px;background:#3b5aa0" aria-label="Social link"></div>
<div class="social abs" style="left:465px;background:#d9453b" aria-label="Social link"></div>
<div class="social abs" style="left:501px;background:#2c9ee0" aria-label="Social link"></div>
<div class="footer-links abs">Privacy policy / Contact us</div>

</body>
</html>
```